" Empresa de Fabricaçao de Tijolos Solo Cimento que esta mudando o foco para venda de sistema construtivo, nao mais de tijolos (chamados Tijolos Ecológicos) "

```html
<!DOCTYPE html>
<html lang="pt-BR">
<head>
<meta charset="utf-8">
<title>Cartão de visitas — Solarbloc</title>
<link rel="stylesheet" href="https://fonts.googleapis.com/css2?family=Montserrat:wght@400;500;700&family=Open+Sans:wght@400;600&display=swap">
<style>
  :root{
    --stage:#ececec;
    --card-dark:#4d5354;
    --card-light:#fbfbfb;
    --olive:#86a125;
    --sun:#f2c318;
    --ink:#5a6163;
    --ink-soft:#666b6d;
    --muted:#b9bcbd;
    --ghost:#eeeeee;
  }
  *{margin:0;padding:0;box-sizing:border-box}
  html,body{width:1200px;height:1200px;overflow:hidden;background:var(--stage)}
  .sheet{position:relative;width:1200px;height:1200px}

  .card{position:absolute;width:773px;height:437px;overflow:hidden}

  /* verso */
  .card-back{left:235px;top:230px;background:var(--card-dark)}
  .card-back .accent{position:absolute;right:0;top:175px;width:14px;height:89px;background:var(--olive)}
  .card-back .mark{position:absolute;left:58px;top:190px;width:64px;height:64px;border-radius:50%;background:var(--sun)}
  .card-back .site{position:absolute;left:168px;top:211px;font:400 17px/1 "Montserrat",sans-serif;letter-spacing:6px;color:var(--muted)}

  /* frente */
  .card-front{left:240px;top:720px;background:var(--card-light)}
  .card-front .ghost{position:absolute;right:-70px;top:130px;width:330px;height:330px;border-radius:50%;background:var(--ghost)}
  .brand{position:absolute;left:60px;top:43px;width:180px;text-align:center}
  .brand .mark{width:103px;height:103px;border-radius:50%;background:var(--sun);margin:0 auto}
  .brand .name{margin-top:17px;font:700 27px/1 "Montserrat",sans-serif;letter-spacing:1.5px;color:var(--ink)}
  .brand .tagline{margin-top:6px;font:500 7px/1 "Montserrat",sans-serif;letter-spacing:1px;color:var(--olive);text-transform:uppercase}

  .holder{position:absolute;left:509px;top:50px;border-left:7px solid var(--olive);padding-left:12px}
  .holder .person{font:500 21px/1.2 "Montserrat",sans-serif;color:var(--ink)}
  .holder .role{font:400 16px/1.3 "Open Sans",sans-serif;color:var(--ink-soft)}

  .contacts{position:absolute;left:60px;top:258px;list-style:none}
  .contacts li{display:flex;align-items:flex-start;gap:10px;margin-bottom:9px;font:400 13.5px/1.35 "Open Sans",sans-serif;color:var(--ink-soft)}
  .contacts .icon{flex:none;width:18px;height:18px;border-radius:4px;background:var(--olive);display:flex;align-items:center;justify-content:center}
  .contacts svg{width:12px;height:12px}
</style>
</head>
<body>
<main class="sheet">

  <section class="card card-back" aria-label="Verso do cartão">
    <span class="mark"></span>
    <p class="site">solarbloc.com.br</p>
    <span class="accent"></span>
  </section>

  <section class="card card-front" aria-label="Frente do cartão">
    <span class="ghost"></span>

    <div class="brand">
      <div class="mark"></div>
      <p class="name">SOLARBLOC</p>
      <p class="tagline">Sistema construtivo sustentável</p>
    </div>

    <div class="holder">
      <p class="person">Nome Sobrenome</p>
      <p class="role">Gerente ADM.</p>
    </div>

    <ul class="contacts">
      <li><span class="icon"><svg viewBox="0 0 12 12"><path d="M6 1a3.5 3.5 0 0 0-3.5 3.5C2.5 7.5 6 11 6 11s3.5-3.5 3.5-6.5A3.5 3.5 0 0 0 6 1zm0 5a1.5 1.5 0 1 1 0-3 1.5 1.5 0 0 1 0 3z" fill="#fff"/></svg></span>
        <span>Endereço completo, Endereço<br>Completo, Endereço Completo</span></li>
      <li><span class="icon"><svg viewBox="0 0 12 12"><rect x="3.5" y="1" width="5" height="10" rx="1" fill="none" stroke="#fff" stroke-width="1.2"/><circle cx="6" cy="9.2" r=".6" fill="#fff"/></svg></span>
        <span>XX XXXX.XXXX | XXXX.XXXX</span></li>
      <li><span class="icon"><svg viewBox="0 0 12 12"><circle cx="6" cy="6" r="2" fill="none" stroke="#fff" stroke-width="1.2"/><path d="M8 4v2.6c0 1 1.6 1.2 1.6-.6A3.6 3.6 0 1 0 7.6 9.2" fill="none" stroke="#fff" stroke-width="1.2"/></svg></span>
        <span>nome@solarbloc.com.br</span></li>
      <li><span class="icon"></span>
        <span>facebook.com/solarbloc</span></li>
    </ul>
  </section>

</main>
</body>
</html>
```